Management consultant needs to update look of website

Currently I have a great word press website but it needs an updated look. I have new text for the site in the attached word document. I also have a list of websites whose design, look, and organization i like as a guide for the designer. The final design should be simple, strong, clear, and project the idea that my brand is a powerful authority in this space. Current site = www.brookfernadvisory.com

Target Market(s)

company owners / executives

Industry/Entity Type

Management Consulting

Number of Pages Required

3 page

Font styles to use
Serif

Colors

Designer to choose colors to be used in the design.

Requirements
Must have
• a simple and clear design and message. professional look. easy navigation. responsive to mobile devices. an easily implemented wordpress theme OR squarespace. use of my logo colors. though I am open to changing to a deep navy or charcoal logo image. source file uploaded.
Nice to have
• i like the cover photo and logo watermark on my current homepage. i like the google map with my logo on the current contact page. i like the animation as well. a great blend of the current site and something that is more seamless.

```html
<!DOCTYPE html>
<html lang="en">
<head>
<meta charset="utf-8">
<title>Brookfern Advisory – Home</title>
<link rel="stylesheet" href="https://fonts.googleapis.com/css2?family=Poppins:wght@400;500;600&family=Great+Vibes&display=swap">
<style>
:root{
  --gold:#dd9a0b;
  --gold-soft:#e3a52a;
  --ink:#1b1b1b;
  --header-bg:#f6f6f6;
  --rule:#1e1e1e;
  --nav-glass:rgba(120,120,120,.55);
  --tab-bg:#f8f7f5;
  --tab-line:#e2dfdb;
  --share-blue-1:#1c5bb8;
  --share-blue-2:#1cb2ea;
  --share-red-1:#e0342a;
  --share-red-2:#d8141f;
  --share-grey:#b5b5b5;
  --share-navy:#0b46c9;
  --guide-red:#e4141c;
}
*{margin:0;padding:0;box-sizing:border-box}
html,body{width:1200px;height:1200px;overflow:hidden;background:#fff;font-family:"Poppins",sans-serif;color:var(--ink)}
.header{position:absolute;left:0;top:272px;width:1200px;height:88px;background:var(--header-bg)}
.brand{position:absolute;left:19px;top:22px;display:flex;align-items:center;gap:12px}
.brand-dot{width:38px;height:38px;border-radius:50%;border:3px solid var(--gold)}
.brand-divider{width:1px;height:46px;background:var(--gold)}
.brand-name{font-size:15px;font-weight:500;color:var(--gold);line-height:1.05;text-transform:uppercase;letter-spacing:.3px}
.brand-tag{font-size:6px;color:var(--gold);margin-top:3px;font-weight:500}
.follow{position:absolute;left:946px;top:24px;display:flex;align-items:center;font-size:11px;font-weight:500}
.follow b{font-weight:600}
.follow span{color:#666;margin-left:3px}
.follow i{display:inline-block;width:18px;height:18px;border-radius:50%;background:#e6e6e6;margin-left:16px}
.follow i:first-of-type{margin-left:24px}
.utility{position:absolute;left:946px;top:50px;font-size:10px;display:flex;gap:12px}
.utility .on{color:var(--gold);border-bottom:2px solid var(--gold);padding-bottom:3px}
.topline{position:absolute;left:0;top:360px;width:1200px;height:6px;background:var(--rule)}
.hero{position:absolute;left:0;top:366px;width:1200px;height:560px;
  background:linear-gradient(180deg,#a9a196 0%,#c9c3b8 30%,#b7ab98 55%,#6f6456 80%,#4b4540 100%)}
.mainnav{position:absolute;left:0;top:366px;width:1150px;height:42px;background:var(--nav-glass)}
.mainnav a{position:absolute;top:13px;color:#fff;font-size:12px;font-weight:500;text-decoration:none}
.mainnav .home{left:16px;top:0;width:94px;height:42px;background:var(--gold);line-height:42px;text-align:center}
.search{position:absolute;left:912px;top:11px;width:178px;height:20px;background:#f3f3f3;border:1px solid #ccc;font-size:10px;color:#555;padding:2px 10px}
.find{position:absolute;left:1090px;top:11px;width:58px;height:20px;background:var(--gold);color:#fff;font-size:10px;text-align:center;line-height:20px}
.arrow-btn{position:absolute;top:601px;width:40px;height:40px;border-radius:50%;background:rgba(255,255,255,.18)}
.arrow-btn svg{position:absolute;left:14px;top:10px}
.dots{position:absolute;left:564px;top:721px;display:flex;gap:11px}
.dots i{width:7px;height:7px;border-radius:50%;background:#fff}
.dots i:first-child{background:var(--gold)}
.motto{position:absolute;left:94px;top:772px;width:205px;height:49px;background:var(--gold-soft);color:#fff;font-family:"Great Vibes",cursive;font-size:31px;line-height:49px;text-align:center;white-space:nowrap}
.headline{position:absolute;left:332px;top:766px;color:#fff;font-size:47px;font-weight:500;text-shadow:0 2px 4px rgba(0,0,0,.35);white-space:nowrap}
.tabs{position:absolute;left:94px;top:848px;width:951px;height:78px;background:var(--tab-bg);display:flex}
.tabs div{height:78px;line-height:78px;text-align:center;font-size:16px;border-right:1px solid var(--tab-line)}
.tabs div:last-child{border-right:0}
.tabs .active{color:var(--gold)}
.share{position:absolute;left:1045px;top:534px;width:58px}
.share div{width:58px;position:relative}
.share svg{position:absolute}
.guides{position:absolute;left:0;top:0}
</style>
</head>
<body>
<header class="header">
  <div class="brand">
    <div class="brand-dot"></div>
    <div class="brand-divider"></div>
    <div>
      <div class="brand-name">Brookfern<br>Advisory</div>
      <div class="brand-tag">Consulting. Training. Speaking.</div>
    </div>
  </div>
  <div class="follow"><b>FOLLOW</b><span>US ON :</span><i></i><i></i><i></i></div>
  <nav class="utility"><span class="on">HOME</span><span>|</span><span>MORE</span><span>|</span><span>HELP</span></nav>
</header>
<div class="topline"></div>

<div class="hero" role="img" aria-label="Photo of a team meeting in a bright loft office, a presenter standing beside a screen"></div>

<nav class="mainnav">
  <a class="home" href="#">HOME</a>
  <a href="#" style="left:142px">ABOUT</a>
  <a href="#" style="left:250px">THE LEDGER BLOG</a>
  <a href="#" style="left:412px">CONTACT</a>
  <div class="search">Search</div>
  <div class="find">FIND</div>
</nav>

<div class="arrow-btn" style="left:24px"><svg width="12" height="20"><path d="M10 2L2 10l8 8" fill="none" stroke="#fff" stroke-width="1.5"/></svg></div>
<div class="arrow-btn" style="left:1137px"><svg width="12" height="20"><path d="M2 2l8 8-8 8" fill="none" stroke="#fff" stroke-width="1.5"/></svg></div>

<div class="dots"><i></i><i></i><i></i><i></i></div>

<div class="motto">I Am Your Guide</div>
<div class="headline">And I’m Here to help</div>

<div class="tabs">
  <div style="width:285px">CONSULTING</div>
  <div class="active" style="width:219px">TRAINING</div>
  <div style="width:228px">SPEAKING</div>
  <div style="width:219px">BLOG</div>
</div>

<div class="share">
  <div style="height:28px;background:var(--gold-soft);border-radius:4px 4px 0 0">
    <svg style="left:24px;top:11px" width="10" height="6"><path d="M1 1l4 4 4-4" fill="none" stroke="#fff" stroke-width="1.5"/></svg>
  </div>
  <div style="height:54px;background:var(--share-blue-1)"></div>
  <div style="height:54px;background:var(--share-blue-2)"></div>
  <div style="height:56px;background:var(--share-red-1)"></div>
  <div style="height:56px;background:var(--share-red-2)"></div>
  <div style="height:55px;background:var(--share-grey)">
    <svg style="left:14px;top:17px" width="30" height="20"><rect x="1" y="1" width="28" height="18" fill="#fff"/><path d="M1 1l14 10 14-10" fill="none" stroke="#ccc" stroke-width="1.5"/></svg>
  </div>
  <div style="height:51px;background:var(--share-navy)"></div>
  <div style="height:38px;background:var(--gold-soft);border-radius:0 0 4px 4px">
    <svg style="left:20px;top:10px" width="18" height="18"><circle cx="14" cy="3" r="2.5" fill="#fff"/><circle cx="4" cy="9" r="2.5" fill="#fff"/><circle cx="14" cy="15" r="2.5" fill="#fff"/><path d="M14 3L4 9l10 6" fill="none" stroke="#fff" stroke-width="1.5"/></svg>
  </div>
</div>

<svg class="guides" width="1200" height="1200">
  <line x1="1029" y1="562" x2="1029" y2="896" stroke="var(--guide-red)" stroke-width="2"/>
  <path d="M1024 563l5-9 5 9z" fill="var(--guide-red)"/>
  <line x1="1121" y1="553" x2="1121" y2="888" stroke="var(--guide-red)" stroke-width="2"/>
  <path d="M1116 887l5 9 5-9z" fill="var(--guide-red)"/>
</svg>
</body>
</html>
```